Business Card for Restaurant Vendal

This project consist of creating 2 design for business card of restaurant named Vendal.

The attached specs below are 'ONLY SUGGESTION' if you have others ideas. You are welcome to post it.

1) Restaurant Card

Adresse:
2784 Côte du Pinard Vert
Montréal (Qc) H4K 3T8

Website:
www.ven-dal.ca

Phone:
438-719-2046

2) Employee Card

Name: Lorna Pik
Title: Owner

Address:
2784 Côte du Pinard Vert
Montréal (Qc) H4K 3T8

Email:lorna@ven-dal.ca
Phone Number:438-719-2046
Cellphone Number:514-830-4162

 The attached specs are 'ONLY SUGGESTION' if you have others ideas.  You are welcome to post it.

Industry/Entity Type

Restaurant

Requirements
Must have
• UV Card Spot

To print Spot UV business cards you would have to submit 2 files for each side. The first file "base" would be your regular design file as it would have been in any other case. The 2nd file "UV mask" is a black/white file. The BLACK color will indicate the areas that will be covered with the UV high gloss finish. To upload the files, please combine front design and front mask file in one P
Nice to have
• 1) The font of the logo should be ink effect
2) black background with wallpaper effect
3) The specs below are 'ONLY SUGGESTION' if you have others ideas. You are welcome to post it.

```html
<!DOCTYPE html>
<html lang="fr">
<head>
<meta charset="utf-8">
<title>Restaurant Vendal — Business Cards</title>
<link rel="stylesheet" href="https://fonts.googleapis.com/css2?family=Source+Sans+3:wght@400;600;700&display=swap">
<style>
  :root {
    --sheet: #ffffff;
    --ink: #111111;
    --card-dark: #1d1d1d;
    --card-dark-edge: #2b2b2b;
    --silver: #d9d9d9;
    --grey-text: #a8a8a8;
    --accent-red: #e0231b;
    --lantern-black: #0a0a0a;
    --card-light: #ffffff;
  }
  * { box-sizing: border-box; margin: 0; padding: 0; }
  html, body {
    width: 1200px; height: 1161px; overflow: hidden;
    background: var(--sheet);
    font-family: "Source Sans 3", Arial, sans-serif;
    color: var(--ink);
  }
  .board { position: relative; width: 1200px; height: 1161px; }

  .section-label { position: absolute; font-size: 16px; font-weight: 400; color: var(--ink); }
  .section-label.restaurant { left: 86px; top: 133px; }
  .section-label.employee { left: 89px; top: 524px; }

  .card { position: absolute; overflow: hidden; box-shadow: 5px 6px 8px rgba(0,0,0,0.35); }
  .card.landscape { width: 492px; height: 281px; }
  .card.portrait { width: 281px; height: 493px; }

  .card.front {
    background: linear-gradient(100deg, var(--card-dark) 0%, var(--card-dark-edge) 55%, var(--card-dark) 100%);
  }
  .card.back { background: var(--card-light); }

  .restaurant-front { left: 88px; top: 178px; }
  .restaurant-back { left: 636px; top: 177px; }
  .employee-front { left: 89px; top: 573px; }
  .employee-back { left: 636px; top: 571px; }

  /* lantern artwork zones */
  .lantern-art { position: absolute; }
  .front .lantern-art {
    left: 0; top: 0; width: 250px; height: 281px;
    background: radial-gradient(ellipse at 35% 58%, var(--lantern-black) 0%, var(--lantern-black) 55%, rgba(10,10,10,0) 72%);
  }
  .restaurant-back .lantern-art {
    left: 283px; top: 0; width: 209px; height: 281px;
    background: radial-gradient(ellipse at 55% 58%, var(--lantern-black) 0%, var(--lantern-black) 60%, rgba(10,10,10,0) 74%);
  }
  .employee-back .lantern-art {
    left: 81px; top: 156px; width: 168px; height: 117px;
    border-radius: 50%;
    background: var(--accent-red);
  }

  /* wordmark */
  .wordmark { position: absolute; display: flex; align-items: center; gap: 12px; }
  .wordmark .name { font-weight: 700; line-height: 1; letter-spacing: 1px; }
  .wordmark .dot { border-radius: 50%; background: var(--accent-red); flex: none; }

  .front .wordmark { left: 218px; top: 82px; }
  .front .wordmark .name { font-size: 68px; color: var(--silver); }
  .front .wordmark .dot { width: 22px; height: 22px; margin-top: 70px; }

  .front .tagline {
    position: absolute; left: 222px; top: 168px; width: 212px;
    text-align: center; font-size: 10.5px; font-weight: 700; color: var(--grey-text);
    line-height: 15px;
  }
  .front .tagline .sep { color: var(--accent-red); padding: 0 2px; }

  .restaurant-back .wordmark { left: 67px; top: 44px; }
  .restaurant-back .wordmark .name { font-size: 34px; color: var(--ink); font-weight: 600; letter-spacing: 3px; }

  .employee-back .wordmark { left: 112px; top: 18px; }
  .employee-back .wordmark .name {
    font-size: 34px; color: var(--ink); font-weight: 600; letter-spacing: 3px;
    writing-mode: vertical-rl;
  }

  .contact { position: absolute; text-align: center; font-size: 12.5px; line-height: 16.5px; color: var(--ink); }
  .contact p + p { margin-top: 16px; }
  .restaurant-back .contact { left: 38px; top: 128px; width: 200px; }
  .employee-back .contact { left: 40px; top: 339px; width: 200px; }

  .role { position: absolute; left: 49px; top: 70px; font-size: 12px; line-height: 16px; color: var(--accent-red); }
</style>
</head>
<body>
<main class="board">

  <h2 class="section-label restaurant">1) Restaurant Card</h2>

  <section class="card landscape front restaurant-front">
    <div class="lantern-art" role="img" aria-label="Large black paper lantern illustration"></div>
    <div class="wordmark"><span class="name">Vendal</span><span class="dot"></span></div>
    <p class="tagline">Resto-Bar Japonais<span class="sep">•</span>Japanese Izakaya<br>Plaza Nord</p>
  </section>

  <section class="card landscape back restaurant-back">
    <div class="wordmark"><span class="name">Vendal</span></div>
    <div class="contact">
      <p>2784 Côte du Pinard Vert<br>Montréal (Qc) H4K 3T8</p>
      <p>Web. www.ven-dal.ca<br>Tel. 438-719-2046</p>
    </div>
    <div class="lantern-art" role="img" aria-label="Black paper lantern illustration with red brush kanji for izakaya"></div>
  </section>

  <h2 class="section-label employee">2) Employee Card</h2>

  <section class="card landscape front employee-front">
    <div class="lantern-art" role="img" aria-label="Large black paper lantern illustration"></div>
    <div class="wordmark"><span class="name">Vendal</span><span class="dot"></span></div>
    <p class="tagline">Resto-Bar Japonais<span class="sep">•</span>Japanese Izakaya<br>Plaza Nord</p>
  </section>

  <section class="card portrait back employee-back">
    <p class="role">Owner<br>Lorna Pik</p>
    <div class="wordmark"><span class="name">Vendal</span></div>
    <div class="lantern-art" role="img" aria-label="Red paper lantern illustration with black brush kanji for izakaya"></div>
    <div class="contact">
      <p>2784 Côte du Pinard Vert<br>Montréal (Qc) H4K 3T8</p>
      <p>Email. lorna@ven-dal.ca<br>Tel. 438-719-2046<br>Cell. 514-830-4162</p>
    </div>
  </section>

</main>
</body>
</html>
```